JT & WE Shearing Pty Ltd

We already have an existing logo created by Lumen Quarry however we have restructured to a company. We would like someone to add Pty Ltd to our business name please.

Colors

Designer to choose only greyscale colors for use in the design.

```html
<!DOCTYPE html>
<html lang="en">
<head>
<meta charset="utf-8">
<title>JT &amp; WE Shearing Pty Ltd — Business Card</title>
<link rel="stylesheet" href="https://fonts.googleapis.com/css2?family=Poppins:wght@400;500;600&display=swap">
<style>
  :root {
    --bg: #1c1c1c;
    --card: #141414;
    --card-edge: #2a2a2a;
    --gloss: #3c3c3c;
    --white: #f2f2f2;
    --muted: #9a9a9a;
    --soft: #c8c8c8;
    --rule: #5a5a5a;
  }
  * { margin: 0; padding: 0; box-sizing: border-box; }
  html, body {
    width: 1200px; height: 800px; overflow: hidden;
    background: var(--bg);
    font-family: "Poppins", sans-serif;
  }
  .stage {
    width: 1200px; height: 800px;
    display: flex; align-items: center; justify-content: center; gap: 60px;
  }
  .card {
    width: 500px; height: 286px;
    background: var(--card);
    border: 1px solid var(--card-edge);
    box-shadow: 0 14px 30px rgba(0,0,0,.55);
    position: relative;
  }
  .card--front { display: flex; align-items: center; justify-content: center; }
  .wordmark {
    display: flex; align-items: center; gap: 10px;
    font-weight: 600; letter-spacing: .5px; white-space: nowrap;
  }
  .wordmark__dot { width: 14px; height: 14px; border-radius: 50%; }
  .card--front .wordmark { color: var(--gloss); font-size: 26px; }
  .card--front .wordmark__dot { background: var(--gloss); }
  .card--back { display: flex; align-items: center; padding: 0 28px; }
  .card--back .wordmark { color: var(--white); font-size: 15px; gap: 7px; }
  .card--back .wordmark__dot { background: var(--white); width: 10px; height: 10px; }
  .divider { width: 1px; height: 190px; background: var(--rule); margin: 0 22px 0 20px; }
  .contact { color: var(--soft); font-size: 11px; line-height: 1.45; }
  .contact__name { color: var(--muted); font-size: 16px; font-weight: 500; line-height: 1.2; }
  .contact__role { color: var(--white); font-size: 11px; margin-bottom: 14px; }
  .contact__company { color: var(--muted); }
  .contact__address { color: var(--white); margin-bottom: 14px; }
  .contact__line { display: flex; align-items: center; gap: 8px; color: var(--white); }
  .contact__line svg { width: 10px; height: 10px; fill: var(--muted); flex: none; }
</style>
</head>
<body>
<main class="stage">
  <section class="card card--front" aria-label="Card front">
    <div class="wordmark"><span class="wordmark__dot"></span>JT &amp; WE Shearing Pty Ltd</div>
  </section>

  <section class="card card--back" aria-label="Card back">
    <div class="wordmark"><span class="wordmark__dot"></span>JT &amp; WE Shearing Pty Ltd</div>
    <div class="divider"></div>
    <div class="contact">
      <p class="contact__name">Daniel Hart</p>
      <p class="contact__role">President</p>
      <p class="contact__company">JT &amp; WE Shearing Pty Ltd</p>
      <p class="contact__address">PO Box 418<br>Kellerby WA 6400</p>
      <p class="contact__line">
        <svg viewBox="0 0 24 24"><path d="M6.6 10.8a15.1 15.1 0 0 0 6.6 6.6l2.2-2.2a1 1 0 0 1 1-.25 11.4 11.4 0 0 0 3.6.57 1 1 0 0 1 1 1V20a1 1 0 0 1-1 1A17 17 0 0 1 3 4a1 1 0 0 1 1-1h3.5a1 1 0 0 1 1 1c0 1.25.2 2.45.57 3.57a1 1 0 0 1-.25 1z"/></svg>
        Sam 0400 512 387
      </p>
      <p class="contact__line">
        <svg viewBox="0 0 24 24"><path d="M2 5h20v14H2z M2 5l10 7 10-7" /></svg>
        crew@jtweshearing.com
      </p>
      <p class="contact__line">
        <svg viewBox="0 0 24 24"><circle cx="12" cy="12" r="10"/></svg>
        www.jtweshearing.com
      </p>
    </div>
  </section>
</main>
</body>
</html>
```